Need simple and modern looking business card with all my information on one side and logo on the other side
Info :
Company name - VELTRIN CONSTRUCTION LLC
Company addres- 418 maple 307th. Dunford hill ny 10583
Email- veltrinllc@pormail.Com
Company phone number 555-318-4096
Cell number- 555-762-0384
Web site - veltrinllc.Com
My name Gerald haverstrom

Target Market(s)

Construction , home improvement, remodeling

Industry/Entity Type

Construction

Contact Information for Business Card

It has to be moder but at the same time simple

Font styles to use
Sans Serif

Colors
0255a3
ffffff
000000
f78f20
b1b1b1
9d9d9d
1b1b1b
33a6d7
ec1f27

Requirements
Must have
• My logo on one side maybe with a some kind of background on the other side all my information
Nice to have
• Some kind of background pictures provided by you .PLEASE HAVE ACCOUNT WITH PIXVALEMOR WILL NOT PAY ANY EXTRA FEES .
Should not have
• Any kind of hamer, nails,screws, helmets itp. Please do not copy the other designs come up with something new.

```html
<!DOCTYPE html>
<html lang="en">
<head>
<meta charset="utf-8">
<title>Veltrin Construction LLC – Business Card</title>
<link rel="stylesheet" href="https://fonts.googleapis.com/css2?family=Raleway:wght@400;500;700;800&display=swap">
<style>
  :root {
    --orange: #f78f20;
    --white: #ffffff;
    --ink: #1b1b1b;
    --black: #000000;
    --grey: #9d9d9d;
    --backdrop: #e6e6e6;
  }
  * { box-sizing: border-box; margin: 0; padding: 0; }
  html, body {
    width: 1200px; height: 900px; overflow: hidden;
    background: var(--backdrop);
    font-family: "Raleway", Arial, sans-serif;
  }
  .canvas { position: relative; width: 1200px; height: 900px; }
  .card {
    position: absolute; left: 260px; width: 680px; height: 389px;
    background: var(--white);
    box-shadow: 0 6px 22px rgba(0,0,0,0.18);
    overflow: hidden;
  }
  .card--front { top: 44px; }
  .card--back { top: 466px; }

  .swoosh { position: absolute; inset: 0; width: 100%; height: 100%; }

  .wordmark {
    position: absolute; color: var(--ink); font-weight: 800;
    text-transform: uppercase; line-height: 1;
  }
  .wordmark__name { display: block; }
  .wordmark__suffix { display: block; }
  .card--front .wordmark { left: 150px; top: 200px; }
  .card--front .wordmark__name { font-size: 86px; letter-spacing: 6px; }
  .card--front .wordmark__suffix { font-size: 27px; letter-spacing: 2.4px; margin-top: 6px; }

  .card--back .wordmark { right: 40px; top: 110px; text-align: right; }
  .card--back .wordmark__name { font-size: 54px; letter-spacing: 4px; }
  .card--back .wordmark__suffix { font-size: 17px; letter-spacing: 1.6px; margin-top: 4px; }

  .holder { position: absolute; left: 64px; top: 32px; }
  .holder__name {
    color: var(--orange); font-weight: 800; font-size: 25px; letter-spacing: 0.5px;
    text-transform: uppercase;
  }
  .holder__email {
    display: flex; align-items: center; gap: 6px;
    color: var(--ink); font-size: 21px; font-weight: 500; margin-top: 2px;
  }
  .divider {
    position: absolute; left: 44px; right: 40px; top: 204px;
    height: 1.5px; background: var(--orange);
  }
  .phones { position: absolute; left: 44px; top: 220px; list-style: none; }
  .phones li {
    display: flex; align-items: center; gap: 8px;
    color: var(--ink); font-size: 27px; font-weight: 400; height: 42px;
  }
  .address {
    position: absolute; right: 40px; top: 221px;
    text-align: right; font-style: normal; color: var(--ink);
    font-size: 25px; line-height: 42px;
  }
  .web-band {
    position: absolute; left: 0; right: 0; bottom: 0; height: 62px;
    background: var(--orange);
    display: flex; align-items: center; justify-content: center; gap: 12px;
    color: var(--white); font-weight: 700; font-size: 30px;
  }
  .icon { flex: none; }
</style>
</head>
<body>
<main class="canvas">

  <section class="card card--front" aria-label="Card front">
    <svg class="swoosh" viewBox="0 0 680 389" aria-hidden="true">
      <path d="M0,215 C150,100 390,34 680,44 L680,0 L290,0 C170,22 60,72 0,112 Z" fill="#f78f20"/>
      <path d="M0,150 C110,86 250,38 430,12" fill="none" stroke="#ffffff" stroke-width="7"/>
      <path d="M20,170 C140,96 300,44 520,20" fill="none" stroke="#ffffff" stroke-width="4"/>
    </svg>
    <div class="wordmark">
      <span class="wordmark__name">Veltrin</span>
      <span class="wordmark__suffix">Construction LLC</span>
    </div>
  </section>

  <section class="card card--back" aria-label="Card back">
    <div class="holder">
      <p class="holder__name">Gerald Haverstrom</p>
      <p class="holder__email">
        <svg class="icon" width="24" height="18" viewBox="0 0 24 18" aria-hidden="true">
          <rect x="1" y="2" width="22" height="14" fill="none" stroke="#f78f20" stroke-width="1.6"/>
          <path d="M1,2 L12,10 L23,2 M1,16 L9,8 M23,16 L15,8" fill="none" stroke="#f78f20" stroke-width="1.4"/>
        </svg>
        veltrinllc@pormail.com
      </p>
    </div>

    <div class="wordmark">
      <span class="wordmark__name">Veltrin</span>
      <span class="wordmark__suffix">Construction LLC</span>
    </div>

    <div class="divider"></div>

    <ul class="phones">
      <li>
        <svg class="icon" width="32" height="32" viewBox="0 0 32 32" aria-hidden="true">
          <circle cx="16" cy="16" r="14" fill="none" stroke="#f78f20" stroke-width="2"/>
          <path d="M11,8 L14,8 L15,12 L13,14 C14,17 15.5,18.5 18,19.5 L20,17.5 L24,18.5 L24,21.5 C24,23 22.5,24 21,24 C15,23 9,17 8.5,11 C8.5,9.5 9.5,8 11,8 Z" fill="none" stroke="#f78f20" stroke-width="1.8" stroke-linejoin="round"/>
        </svg>
        555-318-4096
      </li>
      <li>
        <svg class="icon" width="32" height="32" viewBox="0 0 32 32" aria-hidden="true">
          <circle cx="16" cy="16" r="14" fill="none" stroke="#f78f20" stroke-width="2"/>
          <rect x="11.5" y="8" width="9" height="16" rx="1.5" fill="none" stroke="#f78f20" stroke-width="1.8"/>
          <line x1="14.5" y1="21" x2="17.5" y2="21" stroke="#f78f20" stroke-width="1.6"/>
        </svg>
        555-762-0384
      </li>
    </ul>

    <address class="address">
      418 Maple 307th.<br>
      Dunford Hill, NY 10583
    </address>

    <div class="web-band">
      <svg class="icon" width="30" height="30" viewBox="0 0 30 30" aria-hidden="true">
        <circle cx="15" cy="15" r="13" fill="#ffffff"/>
        <ellipse cx="15" cy="15" rx="5.5" ry="13" fill="none" stroke="#f78f20" stroke-width="1.5"/>
        <line x1="2" y1="15" x2="28" y2="15" stroke="#f78f20" stroke-width="1.5"/>
        <path d="M4.5,8.5 H25.5 M4.5,21.5 H25.5" stroke="#f78f20" stroke-width="1.3"/>
      </svg>
      www.veltrinllc.com
    </div>
  </section>

</main>
</body>
</html>
```